Lume Cosmetics Beauty line

For my website, I would like an elegant, high-end, professional, unique/different design.
On my website I want:
- Home page
- Shop Page - (drop-down adult skincare and teen skincare)
- About Us
- Gallery/ skincare videos section
-Client login page ( add subscription)

Below are pics, please photoshop and make it beautiful for my website
I would like diverse pics of people with my logo products

the theme colors should be the colors of my logo, please make the website warm and inviting.

Industry/Entity Type

Beauty / Cosmetics

Font styles to use
Serif

Requirements
Must have
• color skim, everything in brief.

```html
<!DOCTYPE html>
<html lang="en">
<head>
<meta charset="utf-8">
<title>Lume Cosmetics</title>
<link href="https://fonts.googleapis.com/css2?family=Cormorant+Garamond:wght@400;500;600&family=Raleway:wght@400;500&family=Open+Sans:wght@400;600&display=swap" rel="stylesheet">
<style>
:root{
  --blue:#0a5fb4;
  --blue-deep:#0b4f98;
  --gold:#f5b81e;
  --yellow:#ffc812;
  --ink:#1c1c1c;
  --grey-bg:#f3f3f3;
  --hero-a:#aab3b5;
  --hero-b:#d3d8d8;
  --white:#ffffff;
  --black:#000000;
}
*{margin:0;padding:0;box-sizing:border-box}
html,body{width:1200px;height:3998px;overflow:hidden;background:var(--white)}
body{position:relative;font-family:"Raleway",sans-serif;color:var(--ink)}
.abs{position:absolute}
.serif{font-family:"Cormorant Garamond",serif}
.gold{color:var(--gold)}
.blue{color:var(--blue)}

/* header */
.site-header{position:absolute;left:0;top:0;width:1200px;height:78px;background:var(--white);z-index:3}
.brand-tab{position:absolute;left:0;top:0;width:272px;height:78px;background:var(--blue);clip-path:polygon(0 0,100% 0,92% 100%,0 100%)}
.brand-name{position:absolute;left:24px;top:24px;font-family:"Cormorant Garamond",serif;font-size:25px;line-height:30px;color:var(--white);white-space:nowrap}
.main-nav{position:absolute;left:297px;top:31px;display:flex;gap:30px;font-size:12px;text-transform:uppercase;white-space:nowrap}
.cart-btn{position:absolute;left:955px;top:16px;width:45px;height:45px;border-radius:50%;background:var(--blue)}
.login-btn{position:absolute;left:1018px;top:12px;width:162px;height:52px;border-radius:26px;background:var(--yellow);color:var(--blue-deep);font-family:"Cormorant Garamond",serif;font-weight:600;font-size:17px;display:flex;align-items:center;justify-content:center}

/* hero */
.hero-photo{position:absolute;left:0;top:78px;width:1200px;height:640px;background:linear-gradient(100deg,var(--hero-a) 0%,var(--hero-b) 45%,#6b4d3f 75%,#2b1d17 100%)}
.hero-title{position:absolute;left:68px;top:240px;font-family:"Cormorant Garamond",serif;font-size:56px;font-weight:500;letter-spacing:1px;white-space:nowrap}
.hero-text{position:absolute;left:68px;top:318px;width:500px;font-size:13.5px;line-height:28px;color:var(--white)}
.grad-btn{position:absolute;height:53px;border-radius:27px;background:linear-gradient(180deg,var(--gold),var(--blue));color:var(--white);font-family:"Cormorant Garamond",serif;font-weight:600;font-size:16px;display:flex;align-items:center;justify-content:center;letter-spacing:.3px}

/* categories */
.cat-card{position:absolute;top:784px;width:454px;height:232px}
.cat-card h3{position:absolute;font-family:"Cormorant Garamond",serif;font-size:22px;font-weight:600;letter-spacing:1px;white-space:nowrap}
.cat-card p{position:absolute;width:140px;font-size:13px;line-height:17px;color:#444}
.shop-now{position:absolute;width:92px;height:32px;background:var(--white);font-size:11px;display:flex;align-items:center;justify-content:center;font-family:"Open Sans",sans-serif}

/* about */
.about-heading{position:absolute;left:599px;top:1202px;font-family:"Cormorant Garamond",serif;font-size:33px;letter-spacing:.5px;white-space:nowrap}
.about-text{position:absolute;left:599px;top:1259px;width:474px;font-size:13px;line-height:28px}
.faint-name{position:absolute;left:812px;top:1680px;font-family:"Cormorant Garamond",serif;font-size:46px;line-height:50px;color:#e4e4e4;white-space:nowrap}

/* products */
.products{position:absolute;left:0;top:1753px;width:1200px;height:590px;background:var(--grey-bg);border-top:5px solid var(--blue);border-bottom:5px solid var(--blue)}
.section-title{position:absolute;width:1200px;text-align:center;font-family:"Cormorant Garamond",serif;font-size:33px;letter-spacing:.5px}
.product-card{position:absolute;top:190px;width:214px;height:270px;background:var(--white);box-shadow:0 2px 8px rgba(0,0,0,.08);text-align:center;font-family:"Open Sans",sans-serif}
.product-shot{position:absolute;left:42px;top:20px;width:130px;height:150px}
.product-name{position:absolute;top:186px;width:100%;font-size:17px;font-weight:600}
.product-price{position:absolute;top:218px;width:100%;font-size:18px;color:var(--blue)}
.add-cart{position:absolute;left:85px;top:254px;width:44px;height:44px;border-radius:50%;border:2px solid var(--blue);background:var(--white)}

/* gallery */
.gallery-text{position:absolute;left:200px;top:2483px;width:800px;text-align:center;font-size:14px;line-height:28px}
.tile{position:absolute}

/* badges */
.badges{position:absolute;left:0;top:3212px;width:1200px;height:360px;background:var(--grey-bg)}
.badge{position:absolute;top:100px;width:156px;height:156px;border-radius:50%;border:5px solid}

/* footer */
.site-footer{position:absolute;left:0;top:3540px;width:1200px;height:458px;background:var(--black);color:var(--white)}
.foot-head{position:absolute;top:153px;font-family:"Cormorant Garamond",serif;font-weight:600;font-size:15px;color:var(--gold);letter-spacing:.5px;white-space:nowrap}
.foot-list{position:absolute;list-style:none;font-size:13.5px;line-height:28px}
.foot-list li::before{content:"»";color:var(--gold);margin-right:14px}
.contact-row{position:absolute;left:569px;display:flex;gap:16px;font-size:13.5px;line-height:28px}
.contact-dot{flex:none;width:28px;height:28px;border-radius:50%;background:var(--blue)}
.social{position:absolute;top:252px;width:29px;height:29px;border-radius:50%}
.email-field{position:absolute;left:836px;top:228px;width:254px;height:38px;background:var(--white);color:#777;font-size:11px;padding:12px 12px}
.send-btn{position:absolute;left:1038px;top:228px;width:52px;height:38px;background:var(--blue)}
.chat-btn{position:absolute;left:1021px;top:311px;width:48px;height:48px;border-radius:50%;background:var(--blue)}
.foot-rule{position:absolute;left:120px;top:386px;width:965px;height:1px;background:#555}
.copyright{position:absolute;left:125px;top:400px;font-size:12px;white-space:nowrap}
.legal{position:absolute;left:885px;top:400px;font-size:12px;white-space:nowrap}
</style>
</head>
<body>

<header class="site-header">
  <div class="brand-tab"></div>
  <div class="brand-name">LUME COSMETICS</div>
  <nav class="main-nav">
    <span>Home</span><span>Shop</span><span>Teen Skincare</span><span>Adult Skincare</span><span>About Us</span><span>Gallery</span><span>Contact Us</span>
  </nav>
  <div class="cart-btn">
    <svg width="45" height="45" viewBox="0 0 45 45"><path d="M15 17h3l2 9h9l2-7H19" fill="none" stroke="#ffc812" stroke-width="2"/><circle cx="21" cy="29" r="1.6" fill="#ffc812"/><circle cx="28" cy="29" r="1.6" fill="#ffc812"/></svg>
  </div>
  <div class="login-btn">CLIENT LOGIN</div>
</header>

<section class="hero">
  <div class="hero-photo" role="img" aria-label="Portrait of a woman with long dark curly hair and glowing skin"></div>
  <svg class="abs" style="left:0;top:600px" width="1200" height="130" viewBox="0 0 1200 130">
    <path d="M0 105 C250 20 450 40 650 75 C850 110 1000 130 1200 110 L1200 130 L0 130 Z" fill="#fff"/>
    <path d="M0 105 C250 20 450 40 650 75 C850 110 1000 130 1200 110" fill="none" stroke="#0a5fb4" stroke-width="5"/>
  </svg>
  <h1 class="hero-title"><span class="gold">LUME</span> <span class="blue">COSMETICS</span></h1>
  <p class="hero-text">Lorem ipsum dolor sit amet, consectetur adipiscing elit, sed do eiusmod tempor incididunt ut labore et dolore magna aliqua.</p>
  <div class="grad-btn" style="left:71px;top:408px;width:172px">GET STARTED</div>
</section>

<section class="categories">
  <div class="cat-card" style="left:131px;background:#c2c4b9">
    <div class="abs" style="left:0;top:0;width:190px;height:232px;background:linear-gradient(90deg,#d8c2b3,#c2c4b9)" role="img" aria-label="Woman touching her face with clear skin"></div>
    <h3 style="left:218px;top:44px">ADULT SKINCARE</h3>
    <p style="left:223px;top:84px">Lorem Ipsum is simply dummy text of the printing</p>
    <div class="shop-now" style="left:226px;top:160px">SHOP NOW</div>
  </div>
  <div class="cat-card" style="left:615px;background:var(--yellow)">
    <div class="abs" style="left:264px;top:0;width:190px;height:232px;background:linear-gradient(90deg,var(--yellow),#8a5a3c 60%,#3a2218)" role="img" aria-label="Teenage girl in profile with hair in a bun"></div>
    <h3 style="left:42px;top:44px">TEEN SKINCARE</h3>
    <p style="left:47px;top:84px">Lorem Ipsum is simply dummy text of the printing</p>
    <div class="shop-now" style="left:49px;top:160px">SHOP NOW</div>
  </div>
</section>

<section class="about">
  <svg class="abs" style="left:95px;top:1206px" width="436" height="436" viewBox="0 0 436 436">
    <defs><linearGradient id="ringGrad" x1="0" y1="0" x2="0" y2="1"><stop offset="0" stop-color="#f5b81e"/><stop offset="1" stop-color="#0a5fb4"/></linearGradient></defs>
    <circle cx="218" cy="218" r="218" fill="url(#ringGrad)"/>
  </svg>
  <div class="abs" style="left:113px;top:1224px;width:418px;height:418px;border-radius:50%;background:radial-gradient(circle at 55% 50%,#c69a86,#4a3129 70%)" role="img" aria-label="Close-up of a woman wearing smoky eye makeup"></div>
  <h2 class="about-heading"><span class="gold">ABOUT</span> <span class="blue">LUME COSMETICS</span></h2>
  <p class="about-text">Lorem ipsum dolor sit amet, consectetur adipiscing elit, sed do eiusmod tempor incididunt ut labore et dolore magna aliqua.Sed ut perspiciatis unde omnis iste natus error sit voluptatem accusantium doloremque laudantium, totam rem aperiam, eaque ipsa quae ab illo inventore veritatis et quasi architecto beatae vitae dicta sunt explicabo. Nemo enim ipsam voluptatem quia voluptas sit aspernatur aut odit aut fugit, sed quia consequuntur magni dolores eos qui ratione voluptatem sequi nesciunt. Neque porro quisquam est, qui dolorem ipsum quia dolor sit amet, consectetur, adipisci velit, sed quia non numquam eius modi tempora incidunt ut labore et dolore magnam aliquam quaerat voluptatem. Ut enim ad minima veniam.</p>
  <div class="grad-btn" style="left:599px;top:1583px;width:172px">GET STARTED</div>
  <div class="faint-name">LUME COSMETICS</div>
</section>

<section class="products">
  <h2 class="section-title" style="top:90px"><span class="gold">OUR TOP</span> <span class="blue">PRODUCTS</span></h2>
  <svg class="abs" style="left:78px;top:305px" width="22" height="36" viewBox="0 0 22 36"><path d="M18 3 L4 18 L18 33" fill="none" stroke="#0a5fb4" stroke-width="4"/></svg>
  <svg class="abs" style="left:1098px;top:305px" width="22" height="36" viewBox="0 0 22 36"><path d="M4 3 L18 18 L4 33" fill="none" stroke="#0a5fb4" stroke-width="4"/></svg>

  <div class="product-card" style="left:145px">
    <div class="product-shot" role="img" aria-label="Coral lip gloss tube with swatch" style="background:linear-gradient(135deg,#e9876f,#b8665a)"></div>
    <div class="product-name">Lorem ipsum dolor</div><div class="product-price">$25.00</div><div class="add-cart"></div>
  </div>
  <div class="product-card" style="left:378px">
    <div class="product-shot" role="img" aria-label="Berry lip gloss tube with swatch" style="background:linear-gradient(135deg,#c2386f,#8e4a5a)"></div>
    <div class="product-name">Lorem ipsum dolor</div><div class="product-price">$25.00</div><div class="add-cart"></div>
  </div>
  <div class="product-card" style="left:610px">
    <div class="product-shot" role="img" aria-label="Copper lip gloss tube with swatch" style="background:linear-gradient(135deg,#c8734f,#9a5a48)"></div>
    <div class="product-name">Lorem ipsum dolor</div><div class="product-price">$25.00</div><div class="add-cart"></div>
  </div>
  <div class="product-card" style="left:842px">
    <div class="product-shot" role="img" aria-label="Nude gold lip gloss tube with swatch" style="background:linear-gradient(135deg,#d4a57a,#a7786a)"></div>
    <div class="product-name">Lorem ipsum dolor</div><div class="product-price">$25.00</div><div class="add-cart"></div>
  </div>
</section>

<section class="gallery">
  <h2 class="section-title" style="top:2430px"><span class="gold">OUR</span> <span class="blue">GALLERY</span></h2>
  <p class="gallery-text">Lorem ipsum dolor sit amet, consectetur adipiscing elit, sed do eiusmod tempor incididunt ut labore et dolore magna aliqua.Sed ut perspiciatis unde omnis iste natus error sit voluptatem accusantium .</p>
  <div class="tile" style="left:148px;top:2563px;width:296px;height:190px;background:linear-gradient(135deg,#e6e2dc,#c9bca9)" role="img" aria-label="Skincare tools, brushes and serum bottles on a light surface"></div>
  <div class="tile" style="left:451px;top:2563px;width:297px;height:190px;background:linear-gradient(135deg,#8a5a3c,#3d2519)" role="img" aria-label="Portrait of a woman with curly hair"></div>
  <div class="tile" style="left:756px;top:2563px;width:296px;height:190px;background:linear-gradient(135deg,#d9cfc4,#a9988a)" role="img" aria-label="Two friends applying face masks at home"></div>
  <div class="tile" style="left:148px;top:2761px;width:600px;height:189px;background:linear-gradient(90deg,#3f86d6,#6fb0ea 50%,#e7e5df)" role="img" aria-label="Blue product box on a terrazzo surface"></div>
  <div class="tile" style="left:756px;top:2761px;width:296px;height:387px;background:linear-gradient(160deg,#3a2c22,#1d2a3d 60%,#2f261f)" role="img" aria-label="Skin care kit box video preview"></div>
  <svg class="abs" style="left:885px;top:2937px" width="38" height="38" viewBox="0 0 38 38"><circle cx="19" cy="19" r="18" fill="#fff"/><path d="M15 11 L27 19 L15 27 Z" fill="#111"/></svg>
  <div class="tile" style="left:148px;top:2958px;width:296px;height:190px;background:linear-gradient(135deg,#bcd0de,#7d93a3)" role="img" aria-label="Portrait of a young man with curly hair"></div>
  <div class="tile" style="left:451px;top:2958px;width:297px;height:190px;background:linear-gradient(135deg,#f0ebe4,#c8a46e)" role="img" aria-label="Natural ingredients: honey, lavender, salt and brushes"></div>
</section>

<section class="badges">
  <div class="badge" style="left:133px;border-color:#2a8fd8"></div>
  <div class="badge" style="left:389px;border-color:#8a2c7c"></div>
  <div class="badge" style="left:654px;border-color:#8cc440"></div>
  <div class="badge" style="left:912px;border-color:#e8307a"></div>
</section>

<footer class="site-footer">
  <svg class="abs" style="left:0;top:-10px" width="1200" height="90" viewBox="0 0 1200 90">
    <path d="M0 0 L1200 0 L1200 20 C1000 70 800 80 600 55 C400 30 200 10 0 30 Z" fill="#f3f3f3"/>
    <path d="M0 30 C200 10 400 30 600 55 C800 80 1000 70 1200 20" fill="none" stroke="#0a5fb4" stroke-width="5"/>
  </svg>
  <div class="abs serif" style="left:106px;top:198px;font-size:26px;line-height:30px;color:var(--blue);white-space:nowrap">LUME COSMETICS</div>
  <div class="social" style="left:124px;background:var(--blue)"></div>
  <div class="social" style="left:176px;background:var(--blue)"></div>
  <div class="social" style="left:229px;background:var(--gold)"></div>
  <div class="social" style="left:280px;background:var(--blue)"></div>

  <div class="foot-head" style="left:377px">QUICK LINKS</div>
  <ul class="foot-list" style="left:379px;top:175px">
    <li>Home</li><li>About Us</li><li>Shop</li><li>Gallery</li><li>Contact Us</li>
  </ul>

  <div class="foot-head" style="left:569px">CONTACT US</div>
  <div class="contact-row" style="top:180px"><span class="contact-dot"></span><span>123 Lorem ipsum dolor sit<br>et, consectetur adip.</span></div>
  <div class="contact-row" style="top:250px"><span class="contact-dot"></span><span>123 456 7890</span></div>
  <div class="contact-row" style="top:304px"><span class="contact-dot"></span><span>hello@lumebeauty.example</span></div>

  <div class="foot-head" style="left:847px">SIGN UP FOR OUR NEWSLETTER</div>
  <p class="abs" style="left:836px;top:175px;width:256px;font-size:13.5px;line-height:28px">Lorem ipsum dolor sit amet, consectet ur adipiscing elit, sed do.</p>
  <div class="email-field">Enter The Email</div>
  <div class="send-btn">
    <svg width="52" height="38" viewBox="0 0 52 38"><path d="M18 19 L34 11 L30 28 L25 22 Z" fill="#fff"/></svg>
  </div>
  <div class="chat-btn">
    <svg width="48" height="48" viewBox="0 0 48 48"><ellipse cx="24" cy="23" rx="11" ry="9" fill="#fff"/><circle cx="20" cy="23" r="1.4" fill="#0a5fb4"/><circle cx="24" cy="23" r="1.4" fill="#0a5fb4"/><circle cx="28" cy="23" r="1.4" fill="#0a5fb4"/></svg>
  </div>

  <div class="foot-rule"></div>
  <p class="copyright">© Copyrights 2021 &nbsp;<span class="gold serif">LUME COSMETICS.</span> &nbsp; | &nbsp; All Rights Reserved</p>
  <p class="legal">Privacy policy &nbsp; | &nbsp; Terms of Service</p>
</footer>

</body>
</html>
```